New Website for Consulting Company

Our company needs a fresh web design to help us drive our business forward. We are a consulting and software provider to Airports, Air Traffic Organizations, Builders and Architects. We specialize in analyzing operations, monitoring noise levels and creating software to improve operations, meet customer requirements and improve public relations.
Additional Info:
- Additional requirements can be found in the Web Design Brief
- Logo and logo branding attached
Target Market(s)
Airlines, Airports, Government Agencies, and Real Estate Developers
Industry/Entity Type
Aviation
Coding
Coded - Design and coding required
Number of Pages Required
2 page
Colors
Designer to choose colors to be used in the design.
Requirements
Must have
- - Create a Wordpress Design (Coded - Design and coding required)
- - Designer must provide full implementation/coding depending on the platform chosen by the client (i.e. Wordpress theme, HTML/CSS, etc.)
- - This is a multi-page site; Supporting pages can be formatted the same, but links need to be in place
- - Colors used must be grey scale, black or match the logo. It is not necessary to use all the colors in our logo
Should not have
- We are not looking for an overly bright site. While our logo has 5 different colors, it is not necessary to use all of them.

```html
<!DOCTYPE html>
<html lang="en">
<head>
<meta charset="utf-8">
<title>Corvane International</title>
<link rel="stylesheet" href="https://fonts.googleapis.com/css2?family=Roboto:wght@300;400;500;700&display=swap">
<style>
:root{
  --canvas:#ffffff;
  --nav:#29303a;
  --accent:#2a72b0;
  --accent-light:#4ba3d8;
  --ink:#4a4f55;
  --muted:#8a8f96;
  --rule:#e6e8ea;
  --band-top:#222b36;
  --band-bottom:#0a0f15;
  --footer:#252c36;
  --footer-base:#1c2129;
  --photo-a:#8d949c;
  --photo-b:#3b4048;
}
*{margin:0;padding:0;box-sizing:border-box}
html,body{width:1200px;height:1200px;overflow:hidden;background:var(--canvas);font-family:'Roboto',sans-serif;color:var(--ink)}
.page{position:absolute;left:350px;top:0;width:500px;height:1200px;background:#fff;border-left:1px solid #444;border-right:1px solid #444;overflow:hidden}
.abs{position:absolute}
.nav{left:0;top:0;width:500px;height:20px;background:var(--nav);display:flex;padding-left:73px}
.nav a{color:#c9ced4;font-size:5px;text-decoration:none;line-height:20px;padding:0 6px}
.nav a.active{background:var(--accent);color:#fff}
.hero-photo{left:0;top:20px;width:500px;height:232px;background:linear-gradient(160deg,var(--photo-b),var(--photo-a) 45%,var(--photo-b) 80%,#b8bcc1)}
.hero-card{left:73px;top:20px;width:106px;height:234px;background:#fff;box-shadow:0 2px 4px rgba(0,0,0,.35);padding:0 9px;text-align:center}
.brand{margin-top:22px;font-size:11px;font-weight:700;color:#1f2a44;display:flex;align-items:center;justify-content:center;gap:3px}
.brand i{width:6px;height:6px;background:var(--accent);display:inline-block}
.hero-card h1{margin-top:20px;font-size:9.5px;font-weight:500;line-height:12.5px;color:#3a3f45}
.hero-card p{margin-top:20px;font-size:4.6px;line-height:7px;text-align:justify;color:#333}
.rule{left:68px;width:365px;height:1px;background:var(--rule)}
.section-title{left:0;width:500px;text-align:center;font-size:12px;font-weight:500;color:#4e5358}
.card{top:349px;width:88px;height:101px;background:#fff;box-shadow:0 1px 3px rgba(0,0,0,.18);text-align:center}
.card .thumb{width:56px;height:56px;border-radius:50%;margin:3px auto 0}
.card h3{margin-top:8px;font-size:9.5px;font-weight:500;color:#555;line-height:10px}
.btn{display:inline-block;margin-top:3px;width:50px;height:12px;background:var(--accent);color:#fff;font-size:5px;line-height:12px}
.totop{width:13px;height:12px;background:#b3b6ba;color:#fff;font-size:6px;text-align:center;line-height:12px;left:478px}
.band{left:0;top:525px}
.video{left:69px;top:596px;width:147px;height:82px;background:linear-gradient(135deg,#2b4f8a,#8fa7d2 45%,#1b3a6a)}
.video span{position:absolute;left:5px;top:3px;font-size:5.5px;color:#fff}
.video b{position:absolute;left:67px;top:36px;width:13px;height:9px;background:#222;border-radius:2px}
.band-copy{left:252px;top:553px;width:160px;font-size:4.9px;line-height:8px;color:#d8dde3}
.band-copy p{margin-bottom:8px}
.band-copy ul{list-style:none;padding-left:10px}
.band-copy li::before{content:"• ";color:#fff}
.band-copy li span{color:#e0a030}
.map{left:69px;top:801px;width:238px;height:98px;background:linear-gradient(90deg,#a9cbef 35%,#eceae2 50%,#d6e3c8 85%)}
.address{left:330px;top:816px;width:90px;text-align:center;font-size:5.2px;line-height:8px;color:#666}
.address .here{color:var(--accent-light);font-size:6px;margin-bottom:5px}
.address strong{color:#555}
.testi-title{left:0;top:942px;width:500px;text-align:center;color:var(--accent-light);font-size:10px;font-weight:500}
.quote{top:965px;width:180px;text-align:center;font-size:4.8px;line-height:8px;font-style:italic;color:#777}
.person{top:987px;display:flex;align-items:center;gap:5px;font-size:4.8px;line-height:6px;color:#666}
.person .avatar{width:18px;height:18px;border-radius:50%;background:#c9b8a8}
.person b{color:var(--accent-light);font-weight:500}
.social{left:206px;top:1058px;display:flex;gap:2px}
.social i{width:11px;height:11px;background:var(--accent);display:block}
.footer{left:0;top:1074px;width:500px;height:104px;background:var(--footer)}
.fcol{top:1090px;font-size:5.3px;line-height:8px;color:#9aa2ab;font-weight:300}
.fcol h4{font-weight:400;font-size:6px;color:#aeb5bd;margin-bottom:10px}
.fcol a{display:block;color:var(--accent-light);text-decoration:none;margin-bottom:8.5px}
.search{width:111px;height:13px;background:#fff;color:#999;font-size:4.8px;padding:3px 5px}
.base{left:0;top:1178px;width:500px;height:22px;background:var(--footer-base);text-align:center;font-size:5.3px;line-height:22px;color:#9aa2ab}
</style>
</head>
<body>
<div class="page">
  <div class="abs hero-photo" role="img" aria-label="Aerial photograph of an airport terminal with parked aircraft"></div>
  <nav class="abs nav">
    <a class="active">Home</a><a>Services</a><a>Softwares</a><a>About Us</a><a>Contact Us</a>
  </nav>
  <div class="abs hero-card">
    <div class="brand"><i></i>Corvane</div>
    <h1>SOLVE... COMPLEX NOISE AND AIRSPACE ISSUES</h1>
    <p>Corvane International invents and deploys innovative management and technology solutions that address complex noise and airspace issues for airports and residential communities. With more than two decades of experience and original software solutions, the company identifies problems precisely and solves them through a diagnostic process that mitigates political, community and technical concerns, and builds consensus for ideas and solutions.</p>
  </div>

  <div class="abs rule" style="top:285px"></div>
  <h2 class="abs section-title" style="top:315px">GLOBAL CUSTOMER OPERATIONS</h2>

  <div class="abs card" style="left:66px"><div class="thumb" role="img" aria-label="Photo of a terminal roof structure" style="background:radial-gradient(#d9d2c4,#7c6f5e)"></div><h3>Airports</h3><span class="btn">Know More</span></div>
  <div class="abs card" style="left:160px"><div class="thumb" role="img" aria-label="Photo of a laptop with software" style="background:radial-gradient(#3e5770,#1a2430)"></div><h3>Softwares</h3><span class="btn">Know More</span></div>
  <div class="abs card" style="left:254px"><div class="thumb" role="img" aria-label="Photo of a jet engine" style="background:radial-gradient(#8a9bb0,#1b2028 60%)"></div><h3>Noise &amp;<br>Emissions</h3><span class="btn">Know More</span></div>
  <div class="abs card" style="left:348px"><div class="thumb" role="img" aria-label="Photo of a cockpit view" style="background:linear-gradient(#cfd9e2,#6d7d8e 55%,#2a3440)"></div><h3>visualization</h3><span class="btn">Know More</span></div>

  <div class="abs totop" style="top:386px">^</div>
  <div class="abs rule" style="top:497px"></div>

  <svg class="abs band" width="500" height="212" viewBox="0 0 500 212">
    <defs><linearGradient id="bandFill" x1="0" y1="0" x2="0" y2="1"><stop offset="0" stop-color="#222b36"/><stop offset="1" stop-color="#0a0f15"/></linearGradient></defs>
    <polygon points="0,3 500,23 500,209 0,185" fill="url(#bandFill)"/>
  </svg>
  <div class="abs totop" style="top:545px;background:#3a4149">^</div>
  <div class="abs totop" style="top:703px;background:#1a2028">^</div>

  <div class="abs video" role="img" aria-label="Video still of a glowing flight path over the sea"><span>A quiet evolution in airspace management</span><b></b></div>
  <div class="abs band-copy">
    <p><strong>Corvane International</strong> provides airspace visualization services to airports, governments, and partner corporations throughout the world. Airspace visualization services encompass Corvane's innovative approach to graphically show what airspace looks like, and how aircraft fly within the confines of assigned airspace. Visualizing what has traditionally been shown in 2D into 3D brings into focus how technology changes can greatly benefit the entire airspace system.</p>
    <p>Our airspace visualization services are able to depict aircraft operations in terminal, en route, and transoceanic airspace, all in 3D.</p>
    <p>Our core areas of practice in Airspace include:</p>
    <ul>
      <li><span>–</span> 3D airspace modeling in any radar environment</li>
      <li><span>–</span> New procedure modeling</li>
      <li><span>–</span> Multiple airport/regional modeling scenario</li>
      <li><span>–</span> Public airport displays of air traffic</li>
    </ul>
  </div>

  <div class="abs rule" style="top:766px"></div>
  <div class="abs map" role="img" aria-label="Map showing the office location on the coast"></div>
  <div class="abs address">
    <div class="here">We are Here</div>
    <strong>Corvane International,</strong><br>4810 Harbor View Drive, Suite 300<br>Seaside Point, California 90000
  </div>
  <div class="abs totop" style="top:862px">^</div>

  <div class="abs rule" style="top:933px"></div>
  <div class="abs testi-title">Testimonial</div>
  <p class="abs quote" style="left:68px">Lorem ipsum dolor sit amet, consectetur adipiscing elit. Ut elit tellus, luctus nec ullamcorper mattis, pulvinar dapibus leo.</p>
  <p class="abs quote" style="left:253px">Lorem ipsum dolor sit amet, consectetur adipiscing elit. Ut elit tellus, luctus nec ullamcorper mattis, pulvinar dapibus leo.</p>
  <div class="abs person" style="left:130px"><div class="avatar" role="img" aria-label="Client portrait"></div><div><b>John Doe</b><br>Director,ASDF</div></div>
  <div class="abs person" style="left:316px"><div class="avatar" role="img" aria-label="Client portrait" style="background:#6b5646"></div><div><b>John Doe</b><br>Director,ASDF</div></div>
  <div class="abs totop" style="top:1020px">^</div>

  <div class="abs rule" style="top:1044px"></div>
  <div class="abs social" aria-label="Share links"><i></i><i></i><i></i><i></i><i></i><i></i><i></i></div>

  <footer class="abs footer"></footer>
  <div class="abs fcol" style="left:72px;width:110px">
    <h4>AEROLYS</h4>
    AEROLYS is a web-based application designed to create, evaluate and display flight operations in 3D. This software tool evaluates the acoustic and environmental impacts from new Performance Based Procedures as well as new runways and airfield configurations.
  </div>
  <div class="abs fcol" style="left:195px">
    <h4>SEARCH</h4>
    <div class="search">Search ...</div>
  </div>
  <div class="abs fcol" style="left:319px">
    <h4>Know more about us</h4>
    <a>About Us</a><a>Contact Us</a><a>Services</a>
  </div>
  <div class="abs base">Corvane International</div>
</div>
</body>
</html>
```